A modern, fresh introduction to Buddhism

I need a book cover for an A6 sized book to be used both for ebook and hard copy. The author is a young, modern Buddhist teacher of high standing who has written this short intro to Buddhism in an informal Q & As format using modern, accessible language to convey profound and meaningful ideas to the general public. The author is Tibetan, but teaches worldwide and is very personable and dynamic. The cover should portray this and have a fresh yet authentic feel to it (nothing new-agey!). Please see the author's websites www.norvalemtasheteacher.org and www.pwrt.org for reference, but do not feel that the design must align completely with the website designs.

Target Market(s)

General public both in Europe and America and in Asia ranging from teenagers to the elderly. A really broad audience.

Industry/Entity Type

Teacher

Requirements
Must have
• Please include the following text that on the front cover:

A Window onto Stillness

By Drawa Tsomen Lhundrup

Please include the following on the back cover:

Yunor Trenpa Publications (with attached logo above it)
Nice to have
• A simplistic, artistic, and modern look without any traditional religious images.
Should not have
• No buddha images or religious images. I would prefer a more simplistic, modern and artistic look.

```html
<!DOCTYPE html>
<html lang="en">
<head>
<meta charset="utf-8">
<title>A Window onto Stillness — Cover</title>
<link rel="stylesheet" href="https://fonts.googleapis.com/css2?family=Cinzel:wght@600;700&display=swap">
<style>
  :root {
    --ink-deep: #040606;
    --teal-mist: #2f7a80;
    --teal-glow: #5fb7b0;
    --title-cyan: #8fe6e2;
    --byline-grey: #c9d4d4;
    --line-cyan: #7fd8d0;
    --bokeh-blue: #2a5f86;
    --bokeh-teal: #6fc9c0;
    --bokeh-mint: #a8f0e0;
  }
  * { margin: 0; padding: 0; box-sizing: border-box; }
  html, body {
    width: 783px;
    height: 1200px;
    overflow: hidden;
    background: var(--ink-deep);
  }
  .cover {
    position: relative;
    width: 783px;
    height: 1200px;
    overflow: hidden;
    background: var(--ink-deep);
  }
  .cover-atmosphere {
    position: absolute;
    inset: 0;
    background:
      radial-gradient(ellipse 300px 240px at 420px 760px, rgba(95,183,176,0.45), transparent 70%),
      radial-gradient(ellipse 320px 220px at 160px 420px, rgba(30,80,120,0.55), transparent 70%),
      radial-gradient(ellipse 300px 260px at 640px 880px, rgba(60,140,110,0.35), transparent 70%),
      radial-gradient(ellipse 420px 300px at 330px 640px, rgba(40,110,118,0.45), transparent 70%),
      linear-gradient(180deg, #050707 0%, #060909 22%, #0b2128 40%, #0f3540 58%, #0b2328 78%, #050808 100%);
  }
  .bokeh {
    position: absolute;
    inset: 0;
    width: 783px;
    height: 1200px;
  }
  .bokeh-soft { fill: var(--bokeh-teal); fill-opacity: 0.08; stroke: var(--bokeh-teal); stroke-opacity: 0.35; stroke-width: 0.8; }
  .bokeh-bright { fill: var(--bokeh-mint); fill-opacity: 0.07; stroke: var(--bokeh-mint); stroke-opacity: 0.75; stroke-width: 1.1; }
  .bokeh-blue { fill: var(--bokeh-blue); fill-opacity: 0.45; stroke: var(--bokeh-blue); stroke-opacity: 0.6; stroke-width: 0.8; }
  .bokeh-dot { fill: var(--bokeh-teal); fill-opacity: 0.35; }
  .emblem {
    position: absolute;
    left: 133px;
    top: 86px;
    width: 324px;
    height: 324px;
  }
  .emblem-art {
    position: absolute;
    left: 60px;
    top: 0;
    width: 204px;
    height: 316px;
    border-radius: 102px 102px 20px 20px;
    background: radial-gradient(ellipse at 50% 40%, rgba(127,216,208,0.20), rgba(127,216,208,0.04) 70%);
  }
  .emblem-ring {
    position: absolute;
    inset: 0;
  }
  .title {
    position: absolute;
    left: 0;
    width: 783px;
    top: 544px;
    text-align: center;
    font-family: "Cinzel", serif;
    font-weight: 700;
    font-size: 30px;
    line-height: 36px;
    letter-spacing: 0.5px;
    color: var(--title-cyan);
    text-shadow: 0 0 8px rgba(143,230,226,0.45);
  }
  .byline {
    position: absolute;
    right: 76px;
    top: 604px;
    font-family: "Cinzel", serif;
    font-weight: 600;
    font-size: 15px;
    letter-spacing: 0.5px;
    word-spacing: 6px;
    color: var(--byline-grey);
    text-transform: uppercase;
  }
</style>
</head>
<body>
  <main class="cover">
    <div class="cover-atmosphere"></div>

    <svg class="bokeh" viewBox="0 0 487 747" preserveAspectRatio="none" aria-hidden="true">
      <circle class="bokeh-blue" cx="32" cy="245" r="42"/>
      <circle class="bokeh-blue" cx="95" cy="305" r="30"/>
      <circle class="bokeh-soft" cx="8" cy="290" r="28"/>
      <circle class="bokeh-soft" cx="255" cy="300" r="22"/>
      <circle class="bokeh-soft" cx="365" cy="262" r="22"/>
      <circle class="bokeh-soft" cx="410" cy="325" r="26"/>
      <circle class="bokeh-soft" cx="105" cy="415" r="45"/>
      <circle class="bokeh-soft" cx="140" cy="432" r="38"/>
      <circle class="bokeh-soft" cx="262" cy="392" r="44"/>
      <circle class="bokeh-bright" cx="385" cy="420" r="50"/>
      <circle class="bokeh-soft" cx="445" cy="410" r="34"/>
      <circle class="bokeh-soft" cx="478" cy="445" r="22"/>
      <circle class="bokeh-bright" cx="298" cy="490" r="33"/>
      <circle class="bokeh-soft" cx="298" cy="515" r="19"/>
      <circle class="bokeh-bright" cx="402" cy="532" r="54"/>
      <circle class="bokeh-soft" cx="378" cy="548" r="32"/>
      <circle class="bokeh-bright" cx="155" cy="572" r="54"/>
      <circle class="bokeh-soft" cx="186" cy="560" r="19"/>
      <circle class="bokeh-bright" cx="315" cy="612" r="34"/>
      <circle class="bokeh-soft" cx="440" cy="640" r="30"/>
      <circle class="bokeh-soft" cx="168" cy="700" r="42"/>
      <circle class="bokeh-soft" cx="12" cy="575" r="24"/>
      <circle class="bokeh-soft" cx="60" cy="520" r="14"/>
      <circle class="bokeh-dot" cx="96" cy="455" r="2.5"/>
      <circle class="bokeh-dot" cx="87" cy="498" r="4"/>
      <circle class="bokeh-dot" cx="140" cy="488" r="3"/>
    </svg>

    <div class="emblem">
      <div class="emblem-art" role="img" aria-label="Fine cyan line drawing of a seated figure on a lotus throne"></div>
      <svg class="emblem-ring" viewBox="0 0 324 324" aria-hidden="true">
        <circle cx="162" cy="162" r="160" fill="none" stroke="var(--line-cyan)" stroke-width="1.6"/>
      </svg>
    </div>

    <h1 class="title">A WINDOW ONTO STILLNESS</h1>
    <p class="byline">By Drawa Tsomen Lhundrup</p>
  </main>
</body>
</html>
```